Detox Poster Design Project

I am a naturopath that works in Melbourne. I require a poster that I can put up in my natural therapies clinic that is advertising a detox program that I am offering. The program runs for 3 or 6 weeks and is designed to help your liver, gut and kidney cleanse toxins more efficiently, leaving you feeling energised and healthy.

I would like to see designs that are fresh, organic, clear and contemporary to look at. I want to sell the idea of feeling good, wellbeing and vitality to the potential client. Colours I like include greens, greys and blues.

The final design should communicate health and happiness.

• Please include the photo of the woman in nature.Poster size will be A2 594mm by 420mm
• I have attached the design work for my business cards that you can use. It would be great if the colours and style are in keeping with the existing design work for my business. I have also attached an extra image (almond milk photo) just in case you could see a use for it.

Many thanks.
• No hippy, new age looking design.

```html
<!DOCTYPE html>
<html lang="en">
<head>
<meta charset="utf-8">
<title>Clara Whitfield Naturopath – Sensible Detox Poster</title>
<link rel="stylesheet" href="https://fonts.googleapis.com/css2?family=Fira+Sans:wght@300;400&family=Macondo&family=Italianno&family=Noto+Serif&display=swap">
<style>
  :root {
    --brand-blue: #1b8fcb;
    --panel-blue: #0d5ea6;
    --headline-gold: #f6c417;
    --body-white: #ffffff;
    --contact-green: #8cc63f;
    --mist-light: #eef1ea;
    --mist-leaf: #cfe0a6;
    --sun-haze: #f3f6e4;
    --leaf-bright: #a9cc63;
    --leaf-mid: #5f8f34;
    --leaf-deep: #2e5220;
    --leaf-shadow: #1f3a17;
  }
  * { margin: 0; padding: 0; box-sizing: border-box; }
  html, body { width: 1200px; height: 848px; overflow: hidden; background: #fff; }
  .poster {
    position: relative;
    width: 1200px;
    height: 848px;
    overflow: hidden;
  }

  .brand-area {
    position: absolute;
    left: 0; top: 0;
    width: 574px; height: 370px;
    background:
      radial-gradient(ellipse 220px 120px at 270px 150px, #e3d4c2 0%, rgba(227,212,194,0) 100%),
      radial-gradient(ellipse 200px 160px at 480px 120px, var(--mist-leaf) 0%, rgba(207,224,166,0) 100%),
      radial-gradient(ellipse 180px 90px at 90px 20px, #d4e4a8 0%, rgba(212,228,168,0) 100%),
      linear-gradient(180deg, #e6ecd9 0%, var(--mist-light) 60%, #f4f4f2 100%);
  }
  .brand {
    position: absolute;
    left: 56px; top: 170px;
    display: flex;
    align-items: center;
    gap: 32px;
  }
  .brand-dot {
    width: 82px; height: 82px;
    border-radius: 50%;
    background: var(--brand-blue);
    flex: none;
  }
  .brand-name {
    font-family: "Fira Sans", sans-serif;
    font-weight: 300;
    color: var(--brand-blue);
    line-height: 1;
  }
  .brand-name .name { display: block; font-size: 55px; letter-spacing: -0.5px; }
  .brand-name .role { display: block; font-size: 43px; margin-top: 4px; }

  .offer-panel {
    position: absolute;
    left: 0; top: 370px;
    width: 574px; height: 478px;
    background: var(--panel-blue);
    text-align: center;
  }
  .headline {
    position: absolute;
    left: 0; right: 0; top: 46px;
    font-family: "Macondo", cursive;
    font-weight: 400;
    font-size: 49px;
    line-height: 64px;
    color: var(--headline-gold);
  }
  .pitch {
    position: absolute;
    left: 0; right: 0; top: 130px;
    font-family: "Italianno", cursive;
    font-size: 43px;
    line-height: 43.5px;
    color: var(--body-white);
  }
  .contact {
    position: absolute;
    left: 0; right: 0; top: 363px;
    font-family: "Noto Serif", serif;
    font-size: 20px;
    line-height: 29px;
    color: var(--contact-green);
  }

  .nature-photo {
    position: absolute;
    left: 574px; top: 0;
    width: 626px; height: 848px;
    background:
      radial-gradient(ellipse 240px 200px at 560px 60px, var(--sun-haze) 0%, rgba(243,246,228,0.6) 45%, rgba(243,246,228,0) 100%),
      radial-gradient(ellipse 160px 140px at 60px 110px, rgba(236,242,214,0.9) 0%, rgba(236,242,214,0) 100%),
      radial-gradient(ellipse 180px 260px at 590px 360px, rgba(190,220,110,0.85) 0%, rgba(190,220,110,0) 100%),
      radial-gradient(ellipse 240px 220px at 180px 330px, rgba(31,58,23,0.75) 0%, rgba(31,58,23,0) 100%),
      radial-gradient(ellipse 200px 160px at 90px 560px, rgba(169,204,99,0.7) 0%, rgba(169,204,99,0) 100%),
      radial-gradient(ellipse 160px 240px at 360px 640px, rgba(226,232,214,0.75) 0%, rgba(226,232,214,0) 100%),
      radial-gradient(ellipse 260px 120px at 140px 800px, rgba(120,170,70,0.8) 0%, rgba(120,170,70,0) 100%),
      radial-gradient(ellipse 140px 200px at 600px 760px, rgba(220,236,200,0.7) 0%, rgba(220,236,200,0) 100%),
      linear-gradient(160deg, #8fb45a 0%, var(--leaf-mid) 22%, var(--leaf-deep) 45%, var(--leaf-shadow) 58%, var(--leaf-mid) 78%, var(--leaf-bright) 100%);
  }
</style>
</head>
<body>
  <main class="poster">
    <section class="brand-area" role="img" aria-label="Soft-focus photo of smooth spa stones among fresh green leaves">
      <div class="brand">
        <span class="brand-dot"></span>
        <div class="brand-name">
          <span class="name">Clara Whitfield</span>
          <span class="role">NATUROPATH</span>
        </div>
      </div>
    </section>

    <section class="offer-panel">
      <h1 class="headline">It's Sensible Detox Time</h1>
      <p class="pitch">
        Overindulge over the holidays?<br>
        Have a detox program tailored for you.<br>
        Press reset on your bad eating habits<br>
        to<br>
        feel energised and vital.
      </p>
      <p class="contact">
        For more information contact :<br>
        Clara Whitfield on 0400 123 456<br>
        E-mail: hello@claritynaturopath.com
      </p>
    </section>

    <div class="nature-photo" role="img" aria-label="Photo of a woman seen from behind, arms raised joyfully in a lush sunlit green forest"></div>
  </main>
</body>
</html>
```